Melodex Icon design for single song release

Design an icon for melodex (eventually, we will need to use the same style to design the 4 side CD cover) for a new song to be released. Needs to follow certain specs: I am attaching a design that I created, but looking for the design to be spiced up a bit. I am happy with the design, font, and style.. Just want to see something a bit more creative.
Specs:
1. An Melodex ICON for my latest single that i need to get released. Here are the specs..
• Finalized design for icon for Melodex: (DLT Logo attached and JPEG dimensions below)
o Name of the song is “WHEN”
Melodex: Your cover art must be:
o 1400 x 1400 pixels
o JPG file type
o 72 - 300dpi (300dpi is the best)
o Less than 25mb
o RGB color scheme (not CMYK)

I have my music logo and the picture, so I have to have something that fits these dimensions for Melodex.

Please do not change the photo. and please keep the photo in color. The song has an edge to it, but don't want over the top.

Target Market(s)

Contemporary Christian; Christian Rock - music has an edge.

Font styles to use
Other font styles liked:
• see example design

Requirements
Must have
• Marla Penwick
• Song title "When"
• Photo
• Dimensions listed above when design if final.
• Photo attached
• Logo attached
• *Please use a color photo; please use the lettering like the example; and the font colors

```html
<!DOCTYPE html>
<html lang="en">
<head>
<meta charset="utf-8">
<title>Marla Penwick — When</title>
<link rel="stylesheet" href="https://fonts.googleapis.com/css2?family=Raleway:wght@300&family=Roboto:wght@700&display=swap">
<style>
  :root {
    --frame-line: #e9e3df;
    --name-ink: #f1eae7;
    --title-ink: #ffffff;
    --mark-ink: #f3f1ea;
    --backdrop: #8f8f8f;
  }
  html, body {
    margin: 0;
    padding: 0;
    width: 1200px;
    height: 1200px;
    overflow: hidden;
    background: var(--backdrop);
  }
  .cover {
    display: block;
    width: 1200px;
    height: 1200px;
  }
  .cover__frame {
    fill: none;
    stroke: var(--frame-line);
    stroke-width: 2.5;
  }
  .cover__artist {
    font-family: "Raleway", sans-serif;
    font-weight: 300;
    font-size: 122px;
    fill: var(--name-ink);
  }
  .cover__title {
    font-family: "Roboto", sans-serif;
    font-weight: 700;
    font-size: 138px;
    fill: var(--title-ink);
  }
  .cover__label {
    font-family: "Raleway", sans-serif;
    font-weight: 300;
    font-size: 78px;
    fill: var(--mark-ink);
    letter-spacing: 2px;
  }
</style>
</head>
<body>
<svg class="cover" viewBox="0 0 1200 1200" xmlns="http://www.w3.org/2000/svg">
  <defs>
    <radialGradient id="portraitTones" cx="52%" cy="46%" r="62%">
      <stop offset="0%" stop-color="#d8a184"/>
      <stop offset="38%" stop-color="#cf9a7d"/>
      <stop offset="55%" stop-color="#dcc9a2"/>
      <stop offset="72%" stop-color="#a6a29a"/>
      <stop offset="100%" stop-color="#8c8c8c"/>
    </radialGradient>
  </defs>

  <rect class="cover__portrait" x="0" y="0" width="1200" height="1200" fill="url(#portraitTones)"
        role="img" aria-label="Colour portrait photograph of the artist with blonde hair and a black top against a grey studio backdrop"/>

  <rect class="cover__frame" x="33" y="31" width="1134" height="1136"/>

  <text class="cover__artist" transform="translate(172 1085) rotate(-90)"
        textLength="1005" lengthAdjust="spacingAndGlyphs">MARLA PENWICK</text>

  <text class="cover__label" x="1052" y="160" text-anchor="middle">DLT</text>

  <text class="cover__title" x="1124" y="1088" text-anchor="end">When</text>
</svg>
</body>
</html>
```